Business Cards - Brightway Harbor

need to design unique business card for my mortgage business. I need to design credit card style business card for my business or any unique idea that you might have

Target Market(s)

Home Loan customers

Industry/Entity Type

Mortgage Brokerage

Contact Information for Business Card

please design credit card style or very unique style business card

Colors

Designer to choose colors to be used in the design.

Requirements
Must have
• Name
• position
• Phone number
• fax number
• email address
• website address
• social media address
• All above fields will be provided once design in finalised

```html
<!DOCTYPE html>
<html lang="en">
<head>
<meta charset="utf-8">
<title>Brightway Harbor — Business Cards</title>
<link href="https://fonts.googleapis.com/css2?family=Roboto:ital,wght@0,400;0,500;0,700;1,400&display=swap" rel="stylesheet">
<style>
  :root {
    --stage: #ece7e1;
    --royal: #0b2fb3;
    --paper: #f7f6f3;
    --ink-blue: #1f3fa8;
    --accent-orange: #e8891f;
    --text-grey: #5b5b5b;
    --white: #ffffff;
  }
  * { box-sizing: border-box; margin: 0; padding: 0; }
  html, body {
    width: 1200px; height: 794px; overflow: hidden;
    background: var(--stage);
    font-family: "Roboto", Arial, sans-serif;
  }
  .canvas { position: relative; width: 1200px; height: 794px; }

  .card {
    position: absolute;
    width: 520px; height: 297px;
    border-radius: 3px;
    box-shadow: 0 6px 18px rgba(0,0,0,0.12);
  }

  /* Front card */
  .card--front {
    left: 90px; top: 100px;
    background: var(--royal);
    color: var(--white);
    display: flex; flex-direction: column; align-items: center; justify-content: center;
    padding-left: 40px;
  }
  .brand { display: flex; align-items: center; gap: 10px; }
  .brand__dot { width: 16px; height: 16px; border-radius: 50%; }
  .brand__name { font-weight: 500; font-size: 34px; letter-spacing: 0.5px; }
  .card--front .brand__dot { background: var(--white); }
  .tagline { font-style: italic; font-size: 15px; margin-top: 6px; }
  .card--front .tagline { align-self: center; }
  .social { display: flex; gap: 8px; margin-top: 26px; }
  .social__item { width: 22px; height: 22px; border-radius: 50%; background: var(--white); }

  /* Back card */
  .card--back {
    left: 590px; top: 390px;
    background: var(--paper);
  }
  .card--back .brand {
    position: absolute; right: 34px; top: 42px;
  }
  .card--back .brand__name { color: var(--ink-blue); font-size: 26px; }
  .card--back .brand__dot { background: var(--accent-orange); width: 12px; height: 12px; }
  .card--back .tagline {
    position: absolute; right: 34px; top: 80px;
    color: var(--accent-orange); font-size: 12px; margin: 0;
  }
  .contact {
    position: absolute; right: 30px; top: 150px;
    list-style: none; text-align: right;
    font-size: 12.5px; color: var(--text-grey); line-height: 19px;
  }
  .contact li { display: flex; align-items: center; justify-content: flex-end; gap: 8px; }
  .contact svg { width: 11px; height: 11px; fill: var(--ink-blue); flex: none; }
  .holder { position: absolute; left: 32px; bottom: 30px; }
  .holder__name { color: var(--ink-blue); font-weight: 700; font-size: 17px; }
  .holder__role { color: var(--accent-orange); font-weight: 500; font-size: 12.5px; margin-top: 2px; }
  .holder__address { color: var(--text-grey); font-size: 12.5px; line-height: 17px; margin-top: 8px; }
</style>
</head>
<body>
<main class="canvas">

  <section class="card card--front" aria-label="Business card front">
    <div class="brand">
      <span class="brand__dot"></span>
      <span class="brand__name">Brightway Harbor</span>
    </div>
    <p class="tagline">Steady loans, Sure homes</p>
    <div class="social" aria-label="Social media links">
      <span class="social__item"></span>
      <span class="social__item"></span>
      <span class="social__item"></span>
      <span class="social__item"></span>
    </div>
  </section>

  <section class="card card--back" aria-label="Business card back">
    <div class="brand">
      <span class="brand__dot"></span>
      <span class="brand__name">Brightway Harbor</span>
    </div>
    <p class="tagline">Steady loans, Sure homes</p>

    <ul class="contact">
      <li>555 210 4471
        <svg viewBox="0 0 24 24" aria-hidden="true"><path d="M6.6 10.8a15 15 0 0 0 6.6 6.6l2.2-2.2a1 1 0 0 1 1-.25 11.4 11.4 0 0 0 3.6.57 1 1 0 0 1 1 1V20a1 1 0 0 1-1 1A17 17 0 0 1 3 4a1 1 0 0 1 1-1h3.5a1 1 0 0 1 1 1c0 1.250.2 2.450.57 3.57a1 1 0 0 1-.25 1z"/></svg>
      </li>
      <li>555 318 9026
        <svg viewBox="0 0 24 24" aria-hidden="true"><path d="M6 3h10v5H6zM3 9h18v9h-3v3H6v-3H3zm5 6v4h8v-4z"/></svg>
      </li>
      <li>hello@brightwayharbor.com
        <svg viewBox="0 0 24 24" aria-hidden="true"><path d="M2 5h20v14H2zm2 2v.5l8 5 8-5V7z"/></svg>
      </li>
      <li>www.brightwayharbor.com
        <svg viewBox="0 0 24 24" aria-hidden="true"><path d="M12 2a10 10 0 1 0 0 20 10 10 0 0 0 0-20zm0 2c.9 1.2 1.6 2.9 1.9 5h-3.8c.3-2.1 1-3.8 1.9-5zM4.3 11h3.8a18 18 0 0 0 0 2H4.3a8 8 0 0 1 0-2zm5.8 0h3.8a16 16 0 0 1 0 2h-3.8a16 16 0 0 1 0-2zm5.8 0h3.8a8 8 0 0 1 0 2h-3.8a18 18 0 0 0 0-2zM12 20c-.9-1.2-1.6-2.9-1.9-5h3.8c-.3 2.1-1 3.8-1.9 5z"/></svg>
      </li>
    </ul>

    <div class="holder">
      <p class="holder__name">DANIEL REYES</p>
      <p class="holder__role">CEO/FOUNDER</p>
      <p class="holder__address">4120 Cedar Hollow Road<br>Juneau, Alaska 99801</p>
    </div>
  </section>

</main>
</body>
</html>
```